Awesome photographers card for an awesome new business

Double sided business card Black background and silver logo in middle on one side. Details on otherside. please keep it simple

Photographer

Gavin Tolley
0482615073
GavinTolleyPhotography82@lumenpost.com
www.GavinTolleyPhotography.com.au
Instagram _Gavin_tolley

Requirements
Must have
• My logo in Silver
• please use instagram logo instead of "Instagram"

```html
<!DOCTYPE html>
<html lang="en">
<head>
<meta charset="utf-8">
<title>Gavin Tolley Photography – Business Card</title>
<link href="https://fonts.googleapis.com/css2?family=Open+Sans:wght@400;600&family=Roboto+Condensed:wght@700&display=swap" rel="stylesheet">
<style>
  :root {
    --backdrop: #2f2a27;
    --card: #121212;
    --card-edge: #1c1c1c;
    --silver: #c9c9c9;
    --silver-dim: #8e8e8e;
    --white: #ffffff;
  }
  * { box-sizing: border-box; margin: 0; padding: 0; }
  html, body {
    width: 1200px;
    height: 864px;
    overflow: hidden;
    background: var(--backdrop);
  }
  .sheet {
    position: relative;
    width: 1200px;
    height: 864px;
    display: flex;
    align-items: center;
    justify-content: center;
    gap: 50px;
  }
  .card {
    position: relative;
    width: 525px;
    height: 300px;
    background: var(--card);
    border: 1px solid var(--card-edge);
    border-radius: 4px;
    box-shadow: 0 10px 30px rgba(0,0,0,0.45);
    font-family: "Open Sans", sans-serif;
  }
  .brand {
    display: flex;
    align-items: center;
    justify-content: center;
    gap: 12px;
    color: var(--silver);
    font-family: "Open Sans", sans-serif;
    font-weight: 600;
    font-size: 15px;
    letter-spacing: 2px;
    text-transform: uppercase;
  }
  .brand-ring {
    width: 34px;
    height: 34px;
    border: 2px solid var(--silver);
    border-radius: 50%;
    flex: none;
  }
  .card--front .brand {
    position: absolute;
    left: 0; right: 0;
    top: 120px;
  }
  .card--front .website {
    position: absolute;
    left: 34px;
    bottom: 30px;
    color: var(--silver-dim);
    font-size: 12px;
    letter-spacing: 2px;
  }
  .card--back {
    display: flex;
    flex-direction: column;
    align-items: center;
    padding-top: 58px;
  }
  .card--back .brand { margin-bottom: 26px; }
  .holder-name {
    font-family: "Roboto Condensed", sans-serif;
    font-weight: 700;
    font-size: 19px;
    color: var(--white);
    text-transform: uppercase;
    margin-bottom: 6px;
  }
  .contact {
    list-style: none;
    text-align: center;
    color: var(--white);
    font-size: 13.5px;
    line-height: 1.35;
  }
  .contact .handle {
    display: inline-flex;
    align-items: center;
    gap: 6px;
  }
  .handle-mark {
    width: 10px;
    height: 10px;
    background: var(--white);
    border-radius: 2px;
  }
</style>
</head>
<body>
<main class="sheet">
  <section class="card card--front" aria-label="Card front">
    <div class="brand"><span class="brand-ring"></span><span>Gavin Tolley Photography</span></div>
    <p class="website">www.GavinTolleyPhotography.com.au</p>
  </section>

  <section class="card card--back" aria-label="Card back">
    <div class="brand"><span class="brand-ring"></span><span>Gavin Tolley Photography</span></div>
    <h1 class="holder-name">Gavin Tolley</h1>
    <ul class="contact">
      <li>(P) 0482615073</li>
      <li>GavinTolleyPhotography82@lumenpost.com</li>
      <li>www.GavinTolleyPhotography.com.au</li>
      <li><span class="handle"><span class="handle-mark"></span>_Gavin_tolley</span></li>
    </ul>
  </section>
</main>
</body>
</html>
```